RW dental business card. A family dental practice.

Logo plus the following details.

RW Dental
Dr. Marcus Ellory D.D.S
Family. Implant.Cosmetic

48 Fernbrook Lane, Unit 12-13
Markham, ON K2P7R4

Tel: 905-318-2670
Fx:905-318-9025
rwdental-sample.ca

On the double side:

Next app: ______________________

Please notify us at least 48hours in advance to avoid cancellation fees.

Target Market(s)

Family Dental Services

Industry/Entity Type

Dental

Contact Information for Business Card

Put logo prominently and all the info along with it.

Font styles to use
Other font styles liked:
• See Logo Font

Colors
0255a3
3277b5
85acd3
00a990
33b8a4

Requirements
Must have
• Logo and the info stated above.
• See the logo color scheme.
• Or a grayscale (Black, white gray) combination
Nice to have
• A modern unique layout
Should not have
• too simple a design

```html
<!DOCTYPE html>
<html lang="en">
<head>
<meta charset="utf-8">
<title>RW Dental Business Card</title>
<link href="https://fonts.googleapis.com/css2?family=Tinos:wght@400;700&display=swap" rel="stylesheet">
<style>
  :root {
    --stage-top: #efdfe8;
    --stage-bottom: #cda7bf;
    --stage-edge: #5a2a44;
    --card-white: #ffffff;
    --ink: #3a3a3a;
    --brand-teal: #1fa3a6;
    --brand-blue: #0255a3;
    --tone-light: #d8d6cc;
    --tone-stone: #8f8d78;
    --tone-green: #5a7f45;
    --tone-plum: #463a4c;
    --card-shadow: rgba(110, 30, 80, 0.45);
  }
  * { box-sizing: border-box; margin: 0; padding: 0; }
  html, body { width: 1200px; height: 900px; overflow: hidden; }
  body { position: relative; font-family: "Tinos", "Times New Roman", serif; }
  .stage-top {
    position: absolute; left: 0; top: 0; width: 1200px; height: 476px;
    background: var(--stage-top);
    border-left: 2px solid var(--stage-edge);
    border-top: 2px solid var(--stage-edge);
    border-bottom: 1px solid var(--stage-edge);
  }
  .stage-bottom {
    position: absolute; left: 0; top: 476px; width: 1200px; height: 424px;
    background: var(--stage-bottom);
  }
  .card {
    position: absolute; left: 372px; width: 504px; height: 278px;
    background: var(--card-white);
    box-shadow: 4px 8px 10px var(--card-shadow);
    overflow: hidden;
  }
  .card--front { top: 105px; }
  .card--back { top: 552px; border: 1px solid #555; }
  .card-backdrop {
    position: absolute; left: 0; top: 0; width: 504px;
    background: linear-gradient(90deg, var(--tone-light) 0%, var(--tone-stone) 35%, var(--tone-green) 60%, var(--tone-plum) 85%);
  }
  .card--front .card-backdrop { height: 192px; }
  .card--back .card-backdrop { height: 178px; }
  .brand {
    position: absolute; display: flex; align-items: center; gap: 8px;
    font-weight: 700; font-size: 36px; line-height: 40px;
    color: var(--brand-teal); white-space: nowrap;
  }
  .brand-dot {
    width: 20px; height: 20px; border-radius: 50%;
    background: var(--brand-blue);
  }
  .card--front .brand { left: 262px; top: 96px; }
  .card--back .brand { left: 172px; top: 98px; }
  .practice-heading {
    position: absolute; left: 12px; top: 22px; width: 220px;
    text-align: center; color: #fff; font-weight: 700; font-size: 18px; line-height: 26px;
    text-shadow: -1px -1px 0 #444, 1px -1px 0 #444, -1px 1px 0 #444, 1px 1px 0 #444, 2px 2px 3px rgba(0,0,0,.4);
  }
  .contact, .address, .appointment, .policy {
    position: absolute; color: var(--ink); font-size: 15px; line-height: 18px;
  }
  .contact { left: 15px; top: 204px; }
  .address { left: 262px; top: 218px; font-size: 16px; line-height: 21px; }
  .appointment { left: 15px; top: 190px; font-size: 16px; }
  .policy { left: 15px; top: 228px; width: 390px; font-size: 16px; line-height: 20px; }
</style>
</head>
<body>
  <div class="stage-top"></div>
  <div class="stage-bottom"></div>

  <section class="card card--front">
    <div class="card-backdrop" role="img" aria-label="Decorative flowing swoosh background in grey, green and plum"></div>
    <div class="practice-heading">
      <div>RW Dental</div>
      <div>Dr. Marcus Ellory D.D.S</div>
      <div>Family. Implant.Cosmetic</div>
    </div>
    <div class="brand"><span class="brand-dot"></span>RW Dental</div>
    <div class="contact">
      <div>TEL:905-318-2670</div>
      <div>Fx:905-318-9025</div>
      <div>rwdental-sample.ca</div>
    </div>
    <div class="address">
      <div>48 Fernbrook Lane, Unit 12-13</div>
      <div>Markham, ON K2P7R4</div>
    </div>
  </section>

  <section class="card card--back">
    <div class="card-backdrop" role="img" aria-label="Decorative flowing swoosh background in grey, green and plum"></div>
    <div class="brand"><span class="brand-dot"></span>RW Dental</div>
    <div class="appointment">Next app: ___________________</div>
    <div class="policy">Please notify us at least 48hours in advance to avoid cancellation fees.</div>
  </section>
</body>
</html>
```